Family cosmetic dental practice. Very friendly, relaxed environment. All aspects of modern dentistry with exceptional service.

Industry/Entity Type

Dental

Contact Information for Business Card

Marcus L Fenwick DMD, P.C. 814-561-7094
418 NORTH HALVERTON
ALDER FALLS, PA side2- www.friendlink.com/drmarcusfenwick for news, free KRT Football tickets, promotions, etc.

Requirements
Must have
• face of male and female showing attractive smiles.

```html
<!DOCTYPE html>
<html lang="en">
<head>
<meta charset="utf-8">
<title>Marcus L. Fenwick D.M.D. P.C. – Business Card</title>
<link rel="stylesheet" href="https://fonts.googleapis.com/css2?family=Cinzel:wght@400;500&family=Crimson+Text:wght@400&family=Dancing+Script:wght@400&display=swap">
<style>
  :root {
    --page-bg: #f3f3f3;
    --card-bg: #ffffff;
    --navy: #2f3e5e;
    --ink: #1f1f1f;
    --band-bg: #dfe2e8;
    --band-ink: #3a4868;
    --photo-a: #c9d9ea;
    --photo-b: #e8dcc8;
    --photo-c: #f4efe6;
  }
  * { box-sizing: border-box; margin: 0; padding: 0; }
  html, body {
    width: 1200px; height: 1200px; overflow: hidden;
    background: var(--page-bg);
  }
  .canvas { position: relative; width: 1200px; height: 1200px; }

  .card {
    position: absolute;
    width: 960px; height: 560px;
    background: var(--card-bg);
    box-shadow: 0 2px 10px rgba(0,0,0,0.18);
    overflow: hidden;
    font-family: "Crimson Text", Georgia, serif;
    color: var(--ink);
  }
  .card--front { left: 46px; top: 40px; }
  .card--back  { left: 202px; top: 598px; width: 966px; height: 570px; }

  .photo-area {
    position: absolute; left: 0; top: 0;
    width: 720px; height: 488px;
    background:
      linear-gradient(90deg, rgba(255,255,255,0) 0%, rgba(255,255,255,0) 55%, #ffffff 100%),
      linear-gradient(160deg, var(--photo-c) 0%, var(--photo-a) 40%, var(--photo-b) 75%, var(--photo-c) 100%);
  }

  .name-block {
    position: absolute; right: 38px; top: 28px;
    text-align: right;
    font-family: "Cinzel", "Times New Roman", serif;
    color: var(--navy);
    text-shadow: 1px 2px 3px rgba(0,0,0,0.22);
  }
  .name-block__first { font-size: 58px; line-height: 1; letter-spacing: 1px; }
  .name-block__last  { font-size: 106px; line-height: 0.95; letter-spacing: 1px; }
  .name-block__title {
    font-family: "Crimson Text", Georgia, serif;
    font-size: 30px; line-height: 1.1; letter-spacing: 2px;
    text-shadow: none; margin-right: 4px;
  }

  .front-phone {
    position: absolute; right: 40px; top: 248px;
    font-size: 42px; color: var(--ink);
  }
  .label { font-size: 0.62em; letter-spacing: 1px; }
  .front-address {
    position: absolute; right: 40px; top: 350px;
    text-align: right; font-size: 27px; line-height: 35px;
    font-style: normal;
  }
  .front-web {
    position: absolute; left: 32px; top: 418px;
    font-size: 31px;
  }

  .tagline-band {
    position: absolute; left: 0; bottom: 0;
    width: 100%; height: 72px;
    background: var(--band-bg);
    display: flex; align-items: center; justify-content: center;
    font-size: 22px; letter-spacing: 1px; color: var(--band-ink);
    text-transform: uppercase;
  }

  .back-social {
    position: absolute; left: 40px; top: 246px;
    font-size: 36px;
  }
  .back-promo {
    position: absolute; left: 40px; top: 316px;
    font-family: "Dancing Script", cursive;
    font-size: 42px;
  }
  .back-contact {
    position: absolute; right: 38px; top: 436px;
    font-size: 27px; color: var(--navy);
  }
  .back-contact span + span { margin-left: 14px; }
</style>
</head>
<body>
<main class="canvas">

  <section class="card card--front">
    <div class="photo-area" role="img" aria-label="Photo of a smiling senior couple relaxing together on a porch sofa"></div>

    <div class="name-block">
      <div class="name-block__first">Marcus L.</div>
      <div class="name-block__last">Fenwick</div>
      <div class="name-block__title">D.M.D.&nbsp;&nbsp;P.C.</div>
    </div>

    <div class="front-phone"><span class="label">TEL:</span> 814-561-7094</div>

    <address class="front-address">
      418 N Halverton St<br>
      Alder Falls<br>
      Northvale 40917-2286
    </address>

    <div class="front-web">www.fenwickdental.com</div>

    <div class="tagline-band">Friendly, family cosmetic dental practice with exceptional service</div>
  </section>

  <section class="card card--back">
    <div class="name-block">
      <div class="name-block__first">Marcus L.</div>
      <div class="name-block__last">Fenwick</div>
      <div class="name-block__title">D.M.D.&nbsp;&nbsp;P.C.</div>
    </div>

    <div class="back-social">www.friendlink.com/drmarcusfenwick</div>
    <div class="back-promo">For news, free KRT Football tickets, promotions, etc.</div>

    <div class="back-contact">
      <span><span class="label">TEL:</span> 814-561-7094</span><span>www.fenwickdental.com</span>
    </div>

    <div class="tagline-band">Friendly, family cosmetic dental practice with exceptional service</div>
  </section>

</main>
</body>
</html>
```